Business card for a new cabinet shop company named Marlowe Cabinets for high end cabinets

Design a business card, thinking dark rich green with colours to speak of high end luxury ie; cream, gold, black possibly

Peter Lindqvar
Director Craftsman
Email: info@marlowecabinets.com.au
Instagram : @marlowe.cabinets

```html
<!DOCTYPE html>
<html lang="en">
<head>
<meta charset="utf-8">
<title>Marlowe Cabinets – Business Card</title>
<link href="https://fonts.googleapis.com/css2?family=Montserrat:wght@400;500;700&display=swap" rel="stylesheet">
<style>
  :root {
    --backdrop: #161616;
    --card-green: #1f3d3b;
    --gold: #c9a866;
    --cream: #ffffff;
  }
  * { box-sizing: border-box; margin: 0; padding: 0; }
  html, body {
    width: 1200px;
    height: 1059px;
    overflow: hidden;
    background: var(--backdrop);
    font-family: "Montserrat", sans-serif;
  }
  .card {
    position: absolute;
    left: 258px;
    width: 690px;
    height: 394px;
    background: var(--card-green);
    border-radius: 26px;
  }
  .card-front { top: 99px; }
  .card-back { top: 553px; }

  .wordmark {
    position: absolute;
    display: flex;
    align-items: center;
    gap: 14px;
    color: var(--gold);
    font-weight: 500;
    white-space: nowrap;
  }
  .wordmark-square {
    border: 3px solid var(--gold);
    flex: none;
  }
  .card-front .wordmark {
    left: 55px;
    top: 84px;
    font-size: 34px;
  }
  .card-front .wordmark-square { width: 40px; height: 40px; }
  .card-back .wordmark {
    left: 0;
    right: 0;
    top: 160px;
    justify-content: center;
    font-size: 52px;
    gap: 20px;
  }
  .card-back .wordmark-square { width: 62px; height: 62px; border-width: 4px; }

  .holder {
    position: absolute;
    right: 35px;
    top: 211px;
    text-align: right;
  }
  .holder-name {
    color: var(--gold);
    font-weight: 700;
    font-size: 27px;
    line-height: 34px;
  }
  .holder-role {
    color: var(--cream);
    font-weight: 400;
    font-size: 18.5px;
    line-height: 28px;
    margin-top: 2px;
    letter-spacing: 0.3px;
  }
  .accent-bar {
    position: absolute;
    left: 681px;
    top: 211px;
    width: 9px;
    height: 53px;
    background: var(--gold);
  }
  .divider {
    position: absolute;
    left: 55px;
    top: 298px;
    width: 600px;
    height: 1.5px;
    background: var(--cream);
  }
  .contact {
    position: absolute;
    top: 311px;
    display: flex;
    align-items: center;
    gap: 8px;
    color: var(--cream);
    font-size: 18px;
    letter-spacing: 0.3px;
  }
  .contact-email { left: 52px; }
  .contact-social { right: 35px; }
  .contact svg { flex: none; }
</style>
</head>
<body>
  <section class="card card-front">
    <div class="wordmark">
      <span class="wordmark-square"></span>
      <span class="wordmark-name">Marlowe Cabinets</span>
    </div>

    <div class="holder">
      <p class="holder-name">Peter Lindqvar</p>
      <p class="holder-role">Director Craftsman</p>
    </div>
    <span class="accent-bar"></span>

    <span class="divider"></span>

    <p class="contact contact-email">
      <svg width="18" height="13" viewBox="0 0 18 13" aria-hidden="true">
        <rect x="0" y="0" width="18" height="13" fill="var(--gold)"/>
        <path d="M0 0 L9 7 L18 0" fill="none" stroke="var(--card-green)" stroke-width="1.6"/>
      </svg>
      info@marlowecabinets.com.au
    </p>
    <p class="contact contact-social">
      <svg width="18" height="18" viewBox="0 0 18 18" aria-hidden="true">
        <circle cx="9" cy="9" r="7.5" fill="none" stroke="var(--gold)" stroke-width="2"/>
      </svg>
      @marlowe.cabinets
    </p>
  </section>

  <section class="card card-back">
    <div class="wordmark">
      <span class="wordmark-square"></span>
      <span class="wordmark-name">Marlowe Cabinets</span>
    </div>
  </section>
</body>
</html>
```